Selling High quality Eco-windows. brisklatch.co.uk

I need a logo and website to market and sell high quality triple glazed windows and Tervola Mark certified windows. These windows can be supply only or supply and fit. They are very energy efficient with low U Values. They are made of timber not PVC or metal. I already run a small Eco-building outfit, completing roofing jobs and renovations with attention to quality detailing, energy conservation and renewable energy systems. I am inspired by Scandinavian simplicity and modern architecture. I am a keen environmentalist.

Target Market(s)

Environmentally aware home owners. Wealthier holiday home owners. Eco house projects. Energy efficient renovations.

Industry/Entity Type

Construction

Number of Pages Required

1 page

Font styles to use
Sans Serif

Colors
2fb6a2
ede9f3
3277b5

Requirements
Must have
• Great images. Eco feel but not 'rustic'. Bold and modern but not 'Tall gables'.
• Affordable. Message: "They will save you energy in the long run. Why loose heat through poor quality glazing? These windows will pay for themselves over time in lower energy bills"
• Optimized for tablets and smart phones.
Nice to have
• Scandinavian inspired. Real wood and not plastic.
• See documents below for existing images and colours.
Should not have
• Should not look, earthy, hippy or rustic. But also not incredibly flash Tall Gables style. These windows are affordable to the average person but great quality. They will add value to any building.

```html
<!DOCTYPE html>
<html lang="en">
<head>
<meta charset="utf-8">
<title>Kestrel Glaze – Triple Glazed Timber Windows</title>
<link rel="stylesheet" href="https://fonts.googleapis.com/css2?family=Questrial&family=Open+Sans:wght@400;600;700&display=swap">
<style>
:root{
  --teal:#2fb6a2;
  --teal-dark:#249a89;
  --blue:#3277b5;
  --mist:#ede9f3;
  --dark:#2b2b2b;
  --text:#555;
  --white:#fff;
  --head:'Questrial',sans-serif;
  --body:'Open Sans',sans-serif;
}
*{margin:0;padding:0;box-sizing:border-box}
html,body{width:729px;height:1200px;overflow:hidden}
body{position:relative;background:var(--white);font-family:var(--body);color:var(--text)}
.abs{position:absolute}

/* header */
.site-header{left:0;top:0;width:729px;height:90px;background:var(--dark)}
.header-info{top:29px;font-size:8px;color:#aaa}
.header-email{left:93px}
.header-phone{left:500px}
.brand{left:280px;top:8px;display:flex;align-items:center;gap:10px}
.brand-mark{width:47px;height:47px;border:2px solid var(--teal);border-radius:50%}
.brand-name{font-family:var(--head);font-size:23px;color:var(--teal);letter-spacing:2px;line-height:22px}
.main-nav{left:28px;top:64px;width:671px;height:54px;background:var(--teal);border-radius:4px;display:flex;justify-content:space-around;align-items:center;padding:0 40px}
.main-nav a{font-family:var(--body);font-weight:700;font-size:9px;color:var(--white);text-decoration:none}

/* hero */
.hero{left:0;top:90px;width:729px;height:358px;background:linear-gradient(135deg,#4a4440 0%,#6b625a 40%,#3a3532 100%);z-index:-1}
.hero-title{left:0;top:218px;width:729px;text-align:center;font-family:var(--head);font-weight:400;font-size:34px;line-height:41px;color:var(--white);-webkit-text-stroke:1px var(--white)}
.hero-sub{left:0;top:313px;width:729px;text-align:center;font-size:13px;font-weight:600;color:#6fe0cf}
.btn{display:block;text-align:center;font-size:7px;color:var(--white);background:var(--teal);border-radius:3px;text-decoration:none}
.hero-btn{left:324px;top:354px;width:82px;height:25px;line-height:23px;border:1px solid var(--white)}
.slider-arrows{left:348px;top:430px;width:39px;height:18px;background:#e6e6e6;display:flex;justify-content:center;align-items:center;gap:6px}

/* welcome */
.welcome{left:0;top:448px;width:729px;height:177px;background:var(--mist)}
.section-title{font-family:var(--head);font-size:22px;color:#111;text-align:center;-webkit-text-stroke:.5px #111}
.section-title em{font-style:normal;color:var(--blue);-webkit-text-stroke:.5px var(--blue)}
.welcome-title{left:0;top:30px;width:729px}
.rule{top:45px;height:1px;background:#bbb}
.welcome-text{left:78px;top:71px;width:574px;text-align:center;font-size:7px;line-height:14px}
.welcome-btn{left:324px;top:124px;width:80px;height:24px;line-height:24px}

/* products */
.products-title{left:0;top:648px;width:729px}
.product-label{height:62px;background:var(--teal);color:var(--white);font-family:var(--head);font-size:13px;-webkit-text-stroke:.4px var(--white);display:flex;align-items:center;white-space:nowrap}
.product-desc{border:1px solid var(--teal);font-size:8.5px;line-height:15.5px;padding:17px 16px}
.arrow-btn{width:23px;height:21px;background:var(--teal);border-radius:2px;display:flex;align-items:center;justify-content:center}

/* testimonials */
.testimonials{left:0;top:956px;width:729px;height:202px;background:var(--teal);color:var(--white)}
.testimonials-title{left:0;top:30px;width:729px;font-family:var(--head);font-size:21px;text-align:center;-webkit-text-stroke:.5px var(--white)}
.quote{left:130px;top:75px;width:469px;text-align:center;font-size:7.5px;line-height:17px}
.quote-mark{font-family:Georgia,serif;font-size:20px;font-style:italic;line-height:0}
.quote-author{left:0;top:111px;width:729px;text-align:center;font-size:10px}
.avatars{left:276px;top:137px;display:flex;gap:9px}
.avatar{width:40px;height:40px;border:2px solid var(--white);background:linear-gradient(#3a3a3a,#1d1d1d)}
.avatar.active{background:linear-gradient(#e9e9e9,#bdbdbd)}

/* footer */
.copyright{left:31px;top:1176px;font-size:7px;color:#222}
.social{left:595px;top:1177px;display:flex;gap:12px}
.social span{width:9px;height:9px;border-radius:50%;background:#333}
.social span:first-child{background:var(--blue)}
</style>
</head>
<body>

<header class="abs site-header">
  <p class="abs header-info header-email">Email id : hello@kestrelglaze.co.uk</p>
  <div class="abs brand">
    <span class="brand-mark"></span>
    <span class="brand-name">KESTREL<br>GLAZE</span>
  </div>
  <p class="abs header-info header-phone">Call Us : 020 7946 0321</p>
</header>

<nav class="abs main-nav">
  <a href="#">HOME</a><a href="#">ABOUT US</a><a href="#">OUR PRODUCTS</a><a href="#">GALLERY</a><a href="#">TESTIMONIALS</a><a href="#">CONTACTS</a>
</nav>

<section class="abs hero" role="img" aria-label="Photo of timber window frame sections in a workshop, darkened"></section>
<h1 class="abs hero-title">They Will Save You Energy<br>In The Long Run</h1>
<p class="abs hero-sub">Why lose heat through poor quality glazing?</p>
<a class="abs btn hero-btn" href="#">READ MORE</a>
<div class="abs slider-arrows">
  <svg width="6" height="9" viewBox="0 0 6 9"><path d="M5 1 1 4.5 5 8" fill="none" stroke="#222" stroke-width="1.4"/></svg>
  <svg width="6" height="9" viewBox="0 0 6 9"><path d="M1 1 5 4.5 1 8" fill="none" stroke="#222" stroke-width="1.4"/></svg>
</div>

<section class="abs welcome">
  <div class="abs rule" style="left:28px;width:178px"></div>
  <div class="abs rule" style="left:521px;width:178px"></div>
  <h2 class="abs section-title welcome-title">Welcome to <em>KESTREL GLAZE</em></h2>
  <p class="abs welcome-text">High quality triple glazed timber windows, made from real wood rather than PVC or metal, with very low U values. Supply only or supply and fit. They will save you energy in the long run: why lose heat through poor quality glazing? These windows will pay for themselves over time in lower energy bills, and they are affordable to the average home owner while adding value to any building.</p>
  <a class="abs btn welcome-btn" href="#">READ MORE</a>
</section>

<h2 class="abs section-title products-title">Our <em>Product</em></h2>

<div class="abs product-label" style="left:39px;top:705px;width:228px;padding-left:38px">Triple Glazed Windows</div>
<svg class="abs" style="left:266px;top:723px" width="12" height="18" viewBox="0 0 12 18"><path d="M0 0 11 9 0 18z" fill="#2fb6a2"/></svg>
<p class="abs product-desc" style="left:295px;top:704px;width:394px;height:86px">Lorem ipsum dolor sit amet, consectetur adipiscing elit, sed do eiusmod tempor incididunt ut labore et dolore magna aliqua. Ut enim ad minim veniam, quis nostrud exercitation ullamco laboris nisi ut aliquip ex ea commodo consequat.</p>
<div class="abs arrow-btn" style="left:649px;top:779px"><svg width="6" height="9" viewBox="0 0 6 9"><path d="M1 1 5 4.5 1 8" fill="none" stroke="#fff" stroke-width="1.4"/></svg></div>

<p class="abs product-desc" style="left:40px;top:822px;width:395px;height:87px;text-align:right">Lorem ipsum dolor sit amet, consectetur adipiscing elit, sed do eiusmod tempor incididunt ut labore et dolore magna aliqua. Ut enim ad minim veniam, quis nostrud exercitation ullamco laboris nisi ut aliquip ex ea commodo consequat.</p>
<div class="abs arrow-btn" style="left:63px;top:899px"><svg width="6" height="9" viewBox="0 0 6 9"><path d="M5 1 1 4.5 5 8" fill="none" stroke="#fff" stroke-width="1.4"/></svg></div>
<svg class="abs" style="left:455px;top:840px" width="12" height="18" viewBox="0 0 12 18"><path d="M12 0 1 9 12 18z" fill="#2fb6a2"/></svg>
<div class="abs product-label" style="left:466px;top:822px;width:233px;padding-left:19px">Tervola Mark Certified Windows</div>

<section class="abs testimonials">
  <h2 class="abs testimonials-title">Client Testimonials</h2>
  <p class="abs quote"><span class="quote-mark">“</span> Lorem ipsum dolor sit amet, consectetur adipiscing elit, sed do eiusmod tempor incididunt ut labore et dolore magna aliqua.<br>Ut enim ad minim veniam, quis nostrud exercitation ullamco laboris.<span class="quote-mark">”</span></p>
  <p class="abs quote-author">- ELIN MARSH</p>
  <div class="abs avatars">
    <div class="avatar" role="img" aria-label="Client portrait"></div>
    <div class="avatar" role="img" aria-label="Client portrait"></div>
    <div class="avatar active" role="img" aria-label="Selected client portrait"></div>
    <div class="avatar" role="img" aria-label="Client portrait"></div>
  </div>
</section>

<footer>
  <p class="abs copyright">All Rights Reserved. Copyrights @Kestrel Glaze. 2016</p>
  <div class="abs social" aria-label="Social links">
    <span></span><span></span><span></span><span></span><span></span>
  </div>
</footer>

</body>
</html>
```